Photobook template design

Just one book of 4/5 pages needed to find a handful of designers to help with this project that will be ongoing for several months, we will agree design price per book.

Hi there, we need lots of fabulous photobook templates designed:
there will be 20 books to start with, canvas layouts, calendar layouts etc.

The MAIN idea of the template is to facilitate the easiest creation / ordering of photobooks etc. possible for the client, so all they have to do is upload their pics and drop them into the templates you're going to design...

Each photobook needs to have min 20 pages, there can be a common theme throughout, but they must be different enough so that they do not all blend into one.
Choose to create a design from the following categories:
family
kids
travel
romance / love
seasonal holiday
year in review
everyday / general
recipes
pets / animals
collage
scrapbook

the quality and look and feel must be equal to www.pagelark.com / www.snapvellum.com / www.printorra.co.uk

In order to keep the designs as fresh as possible - we will work with several designers, so for this first project we will choose 1 designer, but then we'll create other design projects for which you will be specifically invited to design for - it's the only way the do multiple designs/projects.

please see 2 pics attached of other templates already designed - we're very happy with these...

Target Market(s)

These photobooks / calendars / canvas prints are for the average family - not too serious, must be fun / tongue in cheek etc.
They're for people who want to do photobooks but have no clue or do not have the time - so they must LOVE the design, and then want to just add their photos...

Industry/Entity Type

Travel

Requirements
Must have
• Must be designed in Layoutra or Vectorix.
Metric sizes please - Either A3 landscape or portrait with 3 mm bleed, or 300 x 300mm square - 3mm bleed
If you place photos for proofing, please use imagewell images - we have a imagewell account

```html
<!DOCTYPE html>
<html lang="en">
<head>
<meta charset="utf-8">
<title>Photobook Template – Fun Page and Spread</title>
<link rel="stylesheet" href="https://fonts.googleapis.com/css2?family=Courier+Prime:wght@700&family=Bitter:wght@700&display=swap">
<style>
  :root {
    --canvas: #ffffff;
    --paper: #efe2c4;
    --paper-deep: #e6d6b2;
    --band-light: #b9dd5e;
    --band-dark: #3f9f6b;
    --teal: #3aa8b7;
    --teal-light: #5cc3cc;
    --green: #8cc440;
    --green-deep: #2f9a5a;
    --photo-slot: #f8fbfc;
    --lol-text: #b9e3e4;
    --label: #111111;
  }
  html, body {
    margin: 0;
    padding: 0;
    width: 1200px;
    height: 1000px;
    overflow: hidden;
    background: var(--canvas);
  }
  .layout {
    position: relative;
    width: 1200px;
    height: 1000px;
  }
  .layout__art {
    position: absolute;
    inset: 0;
    display: block;
  }
  .page-shadow { filter: drop-shadow(2px 4px 5px rgba(0,0,0,0.28)); }
  .item-shadow { filter: drop-shadow(1px 2px 2px rgba(0,0,0,0.22)); }
  .lol-label {
    font-family: "Courier Prime", "Courier New", monospace;
    font-weight: 700;
    font-size: 50px;
    fill: var(--lol-text);
  }
  .spread-label {
    position: absolute;
    left: 921px;
    top: 933px;
    margin: 0;
    font-family: "Bitter", Georgia, serif;
    font-weight: 700;
    font-size: 35px;
    line-height: 1;
    color: var(--label);
  }
</style>
</head>
<body>
<main class="layout">
  <svg class="layout__art" width="1200" height="1000" viewBox="0 0 1200 1000" xmlns="http://www.w3.org/2000/svg">
    <defs>
      <linearGradient id="paper-tone" x1="0" y1="0" x2="1" y2="1">
        <stop offset="0" stop-color="#f1e5c9"/>
        <stop offset="1" stop-color="#eadbb8"/>
      </linearGradient>
      <linearGradient id="trim-tone" x1="0" y1="0" x2="0" y2="1">
        <stop offset="0" stop-color="#2f9a5a"/>
        <stop offset="0.55" stop-color="#3fa7a0"/>
        <stop offset="1" stop-color="#2fa9c0"/>
      </linearGradient>
      <linearGradient id="haha-tone" x1="0" y1="0" x2="1" y2="1">
        <stop offset="0" stop-color="#3aa062"/>
        <stop offset="0.5" stop-color="#7cc4a0"/>
        <stop offset="1" stop-color="#2f9a5a"/>
      </linearGradient>
      <linearGradient id="oval-stripes" x1="0" y1="0" x2="0" y2="1">
        <stop offset="0" stop-color="#9fd06a"/>
        <stop offset="0.3" stop-color="#5cbcc4"/>
        <stop offset="0.6" stop-color="#9fd06a"/>
        <stop offset="1" stop-color="#3aa8b7"/>
      </linearGradient>

      <symbol id="left-page" viewBox="0 0 990 700">
        <rect class="page__paper" width="990" height="700" fill="url(#paper-tone)" role="img" aria-label="Weathered cream paper with soft blue and green polka dots"/>
        <g class="page__band">
          <rect x="0" y="497" width="990" height="105" fill="var(--band-light)"/>
          <rect x="0" y="577" width="990" height="20" fill="var(--band-dark)"/>
        </g>
        <rect class="page__trim" x="178" y="0" width="112" height="700" fill="url(#trim-tone)" role="img" aria-label="Halftone green-to-teal ric-rac ribbon trim"/>
        <rect class="page__haha-tile item-shadow" x="112" y="64" width="224" height="224" transform="rotate(4 224 176)" fill="url(#haha-tone)" role="img" aria-label="Patterned tile of repeated HA lettering in greens and blues"/>
        <circle class="page__dot-halftone" cx="684" cy="412" r="58" fill="var(--green-deep)" role="img" aria-label="Green halftone circle"/>
        <rect class="photo-slot photo-slot--feature item-shadow" x="466" y="90" width="430" height="285" transform="rotate(7.3 681 233)" fill="var(--photo-slot)"/>
        <circle class="page__dot-pin item-shadow" cx="825" cy="88" r="41" fill="var(--green)"/>
        <rect class="photo-slot item-shadow" x="46" y="474" width="160" height="160" fill="var(--photo-slot)"/>
        <rect class="photo-slot item-shadow" x="291" y="398" width="161" height="160" fill="var(--photo-slot)"/>
        <rect class="photo-slot item-shadow" x="481" y="464" width="160" height="160" fill="var(--photo-slot)"/>
        <g class="page__lol-badge item-shadow">
          <circle cx="824" cy="536" r="90" fill="var(--teal)"/>
          <text class="lol-label" x="824" y="555" text-anchor="middle" textLength="150" lengthAdjust="spacingAndGlyphs">LOL :)</text>
        </g>
      </symbol>
    </defs>

    <g class="page page--large page-shadow">
      <use href="#left-page" x="100" y="38" width="990" height="700"/>
    </g>

    <g class="spread page-shadow">
      <use href="#left-page" x="290" y="772" width="297" height="210"/>
      <g class="spread__right-page">
        <rect x="587" y="772" width="297" height="210" fill="url(#paper-tone)" role="img" aria-label="Weathered cream paper with soft blue and green polka dots"/>
        <line x1="587" y1="772" x2="587" y2="982" stroke="var(--paper-deep)" stroke-width="1.5"/>
        <rect x="587" y="921" width="297" height="32" fill="var(--band-light)"/>
        <rect x="587" y="945" width="297" height="6" fill="var(--band-dark)"/>
        <circle cx="691" cy="820" r="36" fill="var(--teal)" role="img" aria-label="Teal halftone circle"/>
        <rect class="photo-slot" x="671" y="803" width="45" height="42" fill="var(--photo-slot)"/>
        <circle cx="612" cy="860" r="13" fill="var(--green)"/>
        <circle cx="631" cy="868" r="10" fill="var(--teal-light)" role="img" aria-label="Small plaid dot"/>
        <ellipse cx="803" cy="874" rx="57" ry="90" fill="url(#oval-stripes)" role="img" aria-label="Striped teal and green oval frame"/>
        <rect class="photo-slot" x="766" y="833" width="75" height="107" fill="var(--photo-slot)"/>
        <circle cx="838" cy="800" r="14" fill="var(--green)" role="img" aria-label="Small flower-shaped accent"/>
        <rect class="photo-slot" x="609" y="898" width="98" height="66" fill="var(--photo-slot)"/>
      </g>
    </g>
  </svg>
  <p class="spread-label">spread</p>
</main>
</body>
</html>
```